Lawn Maintenance Company needs Flyer (Postcard) Design.

Hi everyone.
The majority of what I do is lawn maintenance (grass cutting and trimming/edging).

I'm pretty well open to anything (even humour) but want to stay away from the cartoon/illustration type flyer (but always receptive if you think you have something that might look good, like Pipwren (Quillbys character) :)
Simple but I guess as everyone, something that catches people's eye.

Feel free to kind of play with the name if you think it would help, I would be willing to pay extra if you thought you had a good idea for some type of logo also.

Flyer/Postcard will be front and back, front mainly outlined here, back would be a list of additional services.

Main points I want to get across.
- Professional
- Reliable
- Not like the larger companies that send students or part time
helpers
Kind of want to get those points across without necessarily saying them.

Ok, well, if you haven't rolled your eyes and headed off to the next project.................... :)

Target Market(s)

Mostly regular people with bungalow / two storey houses that don't want to do it themselves and want a nice lawn to frame their house.

Industry/Entity Type

It Company

Requirements
Must have
• Front
** Brightfield Landscaping and Lawn Services
** Lawn Maintenance
** (416) 555-0382
** brightfieldyards@mailtrove.net

Back
Commercial and Residential
Plaza Maintenance
Spring/Fall Clean-up
Fertilizing
Weed Prevention
Hedge Trimming
Flower Bed Design
Topdressing
Triplemix
Overseeding
Lawn & flower bed re-edging
Eavestrough Cleaning
Nice to have
• ummmm....grass. lol :)
Birds
Butterflies
Should not have
• Elaborate homes/gardens
Pictures/photos of people

**The pictures I have included are to just give you an idea of the work I do and the type of properties I do**
Please let me know if you want more pics.

```html
<!DOCTYPE html>
<html lang="en">
<head>
<meta charset="utf-8">
<title>Brightfield Landscaping and Lawn Services – Postcard Front</title>
<link rel="stylesheet" href="https://fonts.googleapis.com/css2?family=Archivo:wght@700&family=Dawning+of+a+New+Day&display=swap">
<style>
  :root {
    --paper: #ffffff;
    --brand-green: #0e6b3b;
    --ink: #231f20;
    --grass-light: #7cc243;
    --grass-mid: #3f9a2c;
    --grass-dark: #1f6b1c;
  }
  * { margin: 0; padding: 0; box-sizing: border-box; }
  html, body { width: 1200px; height: 803px; overflow: hidden; background: var(--paper); }
  .postcard {
    position: relative;
    width: 1200px;
    height: 803px;
    background: var(--paper);
    overflow: hidden;
    font-family: "Archivo", Arial, sans-serif;
  }
  .lawn-art { position: absolute; inset: 0; width: 1200px; height: 803px; }
  .brand {
    position: absolute;
    left: 60px;
    top: 92px;
    color: var(--brand-green);
    font-weight: 700;
    line-height: 1;
  }
  .brand-name { display: block; font-size: 86px; letter-spacing: -1px; }
  .brand-line { display: block; font-size: 22px; letter-spacing: 5px; margin-top: 10px; text-transform: uppercase; }
  .offer {
    position: absolute;
    right: 48px;
    top: 540px;
    text-align: right;
  }
  .tagline {
    font-family: "Dawning of a New Day", cursive;
    font-weight: 400;
    font-size: 66px;
    color: var(--brand-green);
    line-height: 1;
    margin-bottom: 2px;
    margin-right: 30px;
  }
  .service {
    font-size: 27px;
    color: var(--ink);
    line-height: 1.15;
    padding-bottom: 10px;
    border-bottom: 2px solid var(--ink);
  }
  .cta {
    font-size: 31px;
    color: var(--brand-green);
    letter-spacing: 0.3px;
    margin-top: 8px;
    line-height: 1.1;
  }
  .contact {
    font-size: 24.5px;
    color: var(--ink);
    margin-top: 4px;
    line-height: 1.1;
  }
</style>
</head>
<body>
  <main class="postcard">
    <svg class="lawn-art" viewBox="0 0 1200 803" role="img" aria-label="Photographic strips of lush green lawn winding across the card in an S-shaped path">
      <defs>
        <linearGradient id="grass" x1="0" y1="0" x2="0" y2="1">
          <stop offset="0" stop-color="var(--grass-light)"/>
          <stop offset="0.55" stop-color="var(--grass-mid)"/>
          <stop offset="1" stop-color="var(--grass-dark)"/>
        </linearGradient>
      </defs>
      <path class="lawn-strip-upper" fill="url(#grass)"
        d="M665,55 L1151,55 L1151,222 C1100,208 1000,192 900,172 C780,150 662,122 665,55 Z"/>
      <path class="lawn-strip-main" fill="url(#grass)"
        d="M54,362 C250,300 480,292 700,284 C900,276 1050,262 1151,236 L1151,493 C920,496 760,512 610,556 C460,604 330,688 225,746 L54,746 Z"/>
    </svg>

    <header class="brand">
      <span class="brand-name">Brightfield</span>
      <span class="brand-line">Landscaping and Lawn Services</span>
    </header>

    <section class="offer">
      <p class="tagline">Curb Appeal with Every Cut.</p>
      <p class="service">Professional &amp; Reliable Lawn Maintenance</p>
      <p class="cta">CONTACT US FOR A FREE ESTIMATE</p>
      <p class="contact">(416) 555-0382 • brightfieldyards@mailtrove.net</p>
    </section>
  </main>
</body>
</html>
```